Website concept design - need very creative and polished web page layouts

Need 3-4 web pages designed (graphic only). Client is an interior designer and has specific design requirements. Need a skilled graphic designer to help me create a concept for the new site.

The site is primarily meant to allow users to build and buy a new product, but should have a portfolio site feel. I have specific requirements so designer won't have to 'figure it out' on their own.

Making use of white space, text orientation, and object movement are essential to the success of this project.

Inspirational sites:

http://brisk.tamo.site/#en - creative and atypical
https://pembly.io/ - white space and movement; vertical menu links
https://738q.jp- modern into, object hover movement
https://www.polnaxo.com/case-copper-reed - white space, dimensional feel of objects floating on page; pop of color

Target Market(s)

Interior designers and individuals - both commercial and retail.

Industry/Entity Type

Interior Design

Number of Pages Required

4 page

Font styles to use
Serif
Sans Serif

Requirements
Must have
• Professional design, meet design requirements, professional and highly creative look. This cannot look like or resemble in any way a common or typical website. Making use of white space, text orientation, and object movement are essential to the success of this project.
• Colors for the project:
• COLOR TREATMENT - (Not Final)
• DARK PUTTY – 77% Black
• R 95
• G 96
• B 98
• LIGHT PUTTY – 50% Black
• R 129
• G 131
• B 134
• ** Other Levels of Putty can be used.
• BLUE GREEN - (May not be final)
• R 113
• G 202
• B 210
Should not have
• Cannot look like or resemble a typical website design.

```html
<!DOCTYPE html>
<html lang="en">
<head>
<meta charset="utf-8">
<title>Hale Lumen — Welcome</title>
<link href="https://fonts.googleapis.com/css2?family=Lato:wght@300;400;700&display=swap" rel="stylesheet">
<style>
  :root {
    --putty-dark: #5f6062;
    --putty-light: #818386;
    --putty-mid: #6e6f72;
    --blue-green: #71cad2;
    --paper: #ffffff;
    --pattern-base: #eeeeee;
    --text: #555659;
    --line: #d6d7d8;
  }
  * { box-sizing: border-box; margin: 0; padding: 0; }
  html, body { width: 1200px; height: 763px; overflow: hidden; background: var(--paper); }
  body { font-family: "Lato", Arial, sans-serif; color: var(--text); position: relative; }

  .stage-shapes { position: absolute; inset: 0; width: 1200px; height: 763px; }

  .site-header { position: absolute; top: 0; left: 0; width: 1200px; height: 82px; }
  .brand {
    position: absolute; left: 120px; top: 30px;
    font-size: 36px; font-weight: 300; letter-spacing: 1px;
    color: var(--putty-mid); line-height: 1;
  }
  .search {
    position: absolute; left: 572px; top: 34px; width: 234px; height: 32px;
    border: 1px solid #c9cacb; border-radius: 16px;
    display: flex; align-items: center; padding-left: 14px; gap: 8px;
    font-size: 12px; color: #8a8b8d;
  }
  .phone {
    position: absolute; left: 834px; top: 37px;
    display: flex; align-items: center; gap: 5px;
    font-size: 16px; color: #333;
  }
  .cart {
    position: absolute; left: 988px; top: 29px; width: 38px; height: 38px;
    border: 2px solid var(--putty-light); border-radius: 50%;
    display: flex; align-items: center; justify-content: center;
  }
  .menu-toggle { position: absolute; left: 1052px; top: 40px; width: 31px; }
  .menu-toggle span { display: block; height: 2px; background: #8a8b8d; margin-bottom: 5px; }

  .hero-pattern { position: absolute; inset: 0; }

  .welcome-card {
    position: absolute; left: 102px; top: 211px; width: 497px; height: 322px;
    border: 1px solid var(--blue-green);
    text-align: center;
  }
  .welcome-card h1 {
    margin-top: 43px; font-size: 35px; font-weight: 400; color: var(--putty-dark);
    letter-spacing: -0.5px;
  }
  .welcome-card h1 .accent { color: var(--blue-green); }
  .welcome-card p { font-size: 16.5px; line-height: 22px; color: var(--text); }
  .welcome-card .lead { margin-top: 18px; }
  .welcome-card .body { margin-top: 13px; }
  .read-more {
    display: inline-block; margin-top: 22px; width: 166px; height: 42px; line-height: 42px;
    background: var(--putty-dark); color: #fff; font-weight: 700; font-size: 16px;
    text-decoration: none;
  }

  .product-visual {
    position: absolute; left: 620px; top: 112px; width: 470px; height: 436px;
  }

  .site-footer { position: absolute; left: 0; top: 700px; width: 1200px; height: 63px; }
  .copyright { position: absolute; left: 129px; top: 9px; font-size: 14px; color: var(--putty-light); }
  .social { position: absolute; left: 438px; top: 10px; display: flex; gap: 31px; list-style: none; }
  .social li { width: 16px; height: 16px; border-radius: 50%; background: var(--blue-green); }
</style>
</head>
<body>

<svg class="stage-shapes" viewBox="0 0 1200 763" aria-hidden="true">
  <defs>
    <linearGradient id="patternTone" x1="0" y1="0" x2="1" y2="1">
      <stop offset="0" stop-color="#ececec"/>
      <stop offset="0.5" stop-color="#f4f4f4"/>
      <stop offset="1" stop-color="#ebebeb"/>
    </linearGradient>
  </defs>
  <path d="M0 81 L675 110 L1200 102 L1200 720 Q900 700 210 662 L0 697 Z" fill="url(#patternTone)"/>
  <path d="M675 110 L1200 81 L1200 104 Z" fill="var(--putty-light)"/>
  <path d="M675 110 L1200 102 L1200 136 Z" fill="var(--blue-green)"/>
  <path d="M0 650 L205 662 L0 697 Z" fill="var(--putty-dark)"/>
</svg>

<div class="hero-pattern" role="img" aria-label="Soft grey swirling damask wallpaper pattern behind the hero"></div>

<header class="site-header">
  <div class="brand">HALE LUMEN</div>
  <div class="search">
    <svg width="15" height="15" viewBox="0 0 16 16" aria-hidden="true"><circle cx="6.5" cy="6.5" r="5" fill="none" stroke="#b5b6b8" stroke-width="2"/><line x1="10.2" y1="10.2" x2="14.5" y2="14.5" stroke="#b5b6b8" stroke-width="2.2" stroke-linecap="round"/></svg>
    Search here
  </div>
  <div class="phone">
    <svg width="19" height="19" viewBox="0 0 24 24" aria-hidden="true"><path fill="var(--blue-green)" d="M6.6 10.8c1.4 2.8 3.8 5.1 6.6 6.6l2.2-2.2c.3-.3.7-.4 1-.2 1.1.4 2.3.6 3.6.6.6 0 1 .4 1 1V20c0 .6-.4 1-1 1C10.6 21 3 13.4 3 4c0-.6.4-1 1-1h3.5c.6 0 1 .4 1 1 0 1.3.2 2.5.6 3.6.1.3 0 .7-.2 1z"/></svg>
    (800).555.0142
  </div>
  <div class="cart">
    <svg width="18" height="16" viewBox="0 0 24 21" aria-hidden="true"><path fill="var(--blue-green)" d="M0 1h4l1 3h18l-3 9H7l-.6 2H21v2H4l1.6-4L3 3H0z"/><circle cx="7" cy="19" r="2" fill="var(--blue-green)"/><circle cx="19" cy="19" r="2" fill="var(--blue-green)"/></svg>
  </div>
  <div class="menu-toggle" aria-label="Menu"><span></span><span></span><span></span></div>
</header>

<section class="welcome-card">
  <h1>WELCOME <span class="accent">HALE LUMEN</span></h1>
  <p class="lead">Morbi diam mauris viverra in gravida eu mattis in ante<br>Morbi eget arcu Morbi porta libero id ullamcorper</p>
  <p class="body">nonummy nibh ligula pulvinar metus eget consectetuer<br>augue nisi quis lacus Ut ac mi quis lacus mollis aliquam<br>Curabitur iaculis tempus eros Curabitur ve mi</p>
  <a class="read-more" href="#">READ MORE</a>
</section>

<svg class="product-visual" viewBox="0 0 470 436" role="img" aria-label="Two rustic iron cage pendant lamps hanging on chains, a small bell shade and a large round cage">
  <defs>
    <radialGradient id="lampTone" cx="0.5" cy="0.55" r="0.5">
      <stop offset="0" stop-color="#6b6760"/>
      <stop offset="1" stop-color="#8e8a82" stop-opacity="0"/>
    </radialGradient>
  </defs>
  <rect width="470" height="436" fill="url(#lampTone)" opacity="0.55"/>
</svg>

<footer class="site-footer">
  <p class="copyright">© 2018 Company Name&nbsp; All right reserved</p>
  <ul class="social" aria-label="Social links">
    <li></li><li></li><li></li><li></li>
  </ul>
</footer>

</body>
</html>
```